Website design that will showcase a medical assistance tool

I want the medical assistance tool (for hearing aids) website to have a premium or upmarket feel. The brand is Vorquelin (as per attached logo image for guidance). I want the website to appeal to both end users as well as hearing aid clinics.

```html
<!DOCTYPE html>
<html lang="en">
<head>
<meta charset="utf-8">
<title>Vorquelin – Hearing Aid Comfort &amp; Care</title>
<link href="https://fonts.googleapis.com/css2?family=Montserrat:wght@400;500;600&family=Inter:wght@400;500;600&display=swap" rel="stylesheet">
<style>
:root{
  --beige:#cbc4ab;
  --beige-dark:#b9b195;
  --cream:#f3efe2;
  --cream-ring:#e6dfca;
  --ink:#2f2f2f;
  --muted:#6b6b6b;
  --grey-bg:#ebebeb;
  --panel:#efefef;
  --white:#ffffff;
}
*{box-sizing:border-box;margin:0;padding:0}
html,body{width:1200px;height:4135px;overflow:hidden;background:var(--white)}
body{font-family:"Inter",sans-serif;color:var(--ink)}
.page{position:relative;width:1200px;height:4135px;overflow:hidden}
.abs{position:absolute}
.eyebrow{position:absolute;font-family:"Montserrat",sans-serif;font-size:16px;letter-spacing:4px;text-transform:uppercase;color:var(--ink)}
.heading{position:absolute;font-family:"Montserrat",sans-serif;font-weight:500;color:#3a3a3a;line-height:1.1}
.copy{position:absolute;font-size:16px;line-height:25px;color:var(--ink)}
.btn{position:absolute;background:var(--beige);color:var(--white);border-radius:30px;font-family:"Montserrat",sans-serif;font-weight:600;font-size:13px;letter-spacing:1px;display:flex;align-items:center;justify-content:center;text-transform:uppercase}
.photo{position:absolute}
.brand{display:flex;align-items:center;gap:8px;font-family:"Montserrat",sans-serif;font-weight:400;color:#555}
.brand-dot{width:30px;height:30px;border-radius:50%;background:var(--beige)}

/* nav */
.nav{position:absolute;top:0;left:0;width:1200px;height:77px;background:var(--white)}
.nav .brand{position:absolute;left:98px;top:18px;font-size:34px}
.nav-links{position:absolute;left:367px;top:32px;display:flex;gap:44px;font-size:14px}
.nav-cta{position:absolute;left:878px;top:28px;width:104px;height:28px;border-radius:14px;background:var(--beige);color:#fff;font-size:13px;display:flex;align-items:center;justify-content:center}
.social{display:flex;gap:6px}
.social span{width:22px;height:22px;border-radius:50%;background:#888}
.nav .social{position:absolute;left:1008px;top:29px}

/* benefits */
.feature{position:absolute;width:330px}
.feature h3{font-size:18px;font-weight:600;margin-bottom:4px}
.feature p{font-size:15px;color:var(--muted)}
.feature.left{text-align:right}
.icon-badge{position:absolute;width:88px;height:88px;border-radius:50%;background:var(--white);border:8px solid var(--cream-ring)}
.icon-badge::after{content:"";position:absolute;inset:6px;border-radius:50%;background:var(--beige)}

/* testimonials */
.t-side{position:absolute;background:var(--white);border-radius:10px;font-size:11px;line-height:16px;color:#555;text-align:center;padding:46px 20px}
.t-main{position:absolute;left:292px;top:2795px;width:643px;height:277px;background:var(--beige);border-radius:10px;color:var(--white);text-align:center}
.arrow{position:absolute;width:44px;height:44px;border-radius:50%;background:var(--beige);display:flex;align-items:center;justify-content:center}

/* contact */
.contact-item{position:absolute;left:152px;display:flex;align-items:center;gap:10px;font-size:16px;line-height:22px}
.ci-icon{width:40px;height:40px;border-radius:50%;background:var(--beige);display:flex;align-items:center;justify-content:center;flex:none}
.field{position:absolute;background:var(--white);font-size:12px;color:#555;padding:14px 20px}

/* footer */
.footer{position:absolute;top:3730px;left:0;width:1200px;height:405px;background:var(--cream)}
.f-title{position:absolute;font-size:19px;font-weight:600;color:#3a3a3a}
.f-list{position:absolute;list-style:none;font-size:13px;line-height:22px;color:#555}
.f-item{position:absolute;display:flex;align-items:center;gap:8px;font-size:12px;line-height:15px;color:#555}
.f-item .ci-icon{width:28px;height:28px}
</style>
</head>
<body>
<div class="page">

  <!-- Navigation -->
  <header class="nav">
    <div class="brand"><span class="brand-dot"></span>vorquelin</div>
    <nav class="nav-links"><span>Home</span><span>For Individuals</span><span>For Clinics</span><span>About</span><span>Support</span></nav>
    <div class="nav-cta">Contact</div>
    <div class="social"><span></span><span></span><span></span></div>
  </header>

  <!-- Hero -->
  <section class="hero">
    <div class="abs" style="left:0;top:77px;width:1200px;height:670px;background:#f1f0ef"></div>
    <div class="photo" role="img" aria-label="Smiling senior woman being fitted with a behind-the-ear hearing aid" style="left:520px;top:77px;width:680px;height:660px;background:linear-gradient(100deg,#f1f0ef 0%,#d9d5d0 30%,#c9b8a8 55%,#7fb8c0 80%,#e8eef0 100%)"></div>
    <svg class="abs" style="left:0;top:600px" width="1200" height="160" viewBox="0 0 1200 160">
      <path d="M0 20 C300 140 800 140 1200 40 L1200 160 L0 160 Z" fill="#fff"/>
      <path d="M0 20 C300 140 800 140 1200 40 L1200 55 C800 150 300 150 0 45 Z" fill="var(--beige)"/>
    </svg>
    <div class="eyebrow" style="left:114px;top:232px">Welcome to Vorquelin</div>
    <h1 class="heading" style="left:112px;top:256px;font-size:46px;line-height:48px">A New Standard<br>in Hearing Aid<br>Comfort &amp; Care</h1>
    <p class="copy" style="left:113px;top:414px;width:400px">Lorem ipsum dolor sit amet, consectetur adipisc-ing elit sed do eiusmod tempor incididunt</p>
    <div class="btn" style="left:117px;top:490px;width:216px;height:52px;font-size:15px">Try it now &rarr;</div>
  </section>

  <!-- About -->
  <section class="about">
    <div class="photo" role="img" aria-label="Senior woman cupping her ear and smiling" style="left:70px;top:785px;width:510px;height:585px;background:linear-gradient(180deg,#ececec,#d8d4cf 60%,#f0eeea)"></div>
    <div class="abs" style="left:870px;top:1000px;width:330px;height:330px;border-radius:50%;background:#f6f4ee"></div>
    <div class="eyebrow" style="left:604px;top:858px">About Vorquelin</div>
    <h2 class="heading" style="left:598px;top:888px;font-size:40px">About the Technology</h2>
    <p class="copy" style="left:603px;top:960px;width:520px">Lorem ipsum dolor sit amet, consectetur adipiscing elit, sed do eiusmod tempor incididunt ut labore et dolore magna</p>
    <p class="copy" style="left:603px;top:1035px;width:520px">Lorem ipsum dolor sit amet, consectetur adipiscing elit, sed do eiusmod tempor incididunt ut labore et dolore magna aliqua. Quis ipsum suspendisse ultrices gravid Risus comm</p>
    <div class="btn" style="left:599px;top:1145px;width:163px;height:45px">Learn more</div>
  </section>

  <!-- Benefits -->
  <section class="benefits">
    <svg class="abs" style="left:0;top:1280px" width="1200" height="735" viewBox="0 0 1200 735">
      <path d="M0 80 C300 0 900 0 1200 95 L1200 620 C900 740 300 740 0 625 Z" fill="var(--cream)"/>
      <path d="M0 625 C300 740 900 740 1200 620 L1200 600 C900 725 300 725 0 600 Z" fill="var(--beige)"/>
      <path d="M0 80 C300 0 900 0 1200 95 L1200 110 C900 15 300 15 0 95 Z" fill="var(--beige)"/>
    </svg>
    <div class="photo" role="img" aria-label="Beige behind-the-ear hearing aid device" style="left:945px;top:1180px;width:150px;height:190px;border-radius:60px;background:linear-gradient(160deg,#f2f2f2,#d5c9a7 50%,#a89b77)"></div>
    <div class="eyebrow" style="left:0;width:1200px;text-align:center;top:1375px">Why choose us</div>
    <h2 class="heading" style="left:0;width:1162px;text-align:center;top:1400px;font-size:40px">Benefits &amp; Features</h2>

    <div class="abs" style="left:410px;top:1505px;width:360px;height:360px;border-radius:50%;background:var(--cream-ring)"></div>
    <div class="abs" style="left:430px;top:1525px;width:320px;height:320px;border-radius:50%;background:#ded6bd"></div>
    <div class="abs" style="left:470px;top:1580px;width:236px;height:236px;border-radius:50%;background:var(--white);display:flex;flex-direction:column;align-items:center;justify-content:center;font-family:'Montserrat',sans-serif;font-size:44px;color:#555">
      <span class="brand-dot" style="width:40px;height:40px;margin-bottom:6px"></span>vorquelin
    </div>

    <div class="icon-badge" style="left:399px;top:1510px"></div>
    <div class="icon-badge" style="left:689px;top:1510px"></div>
    <div class="icon-badge" style="left:355px;top:1638px"></div>
    <div class="icon-badge" style="left:732px;top:1638px"></div>
    <div class="icon-badge" style="left:396px;top:1785px"></div>
    <div class="icon-badge" style="left:692px;top:1777px"></div>

    <div class="feature left" style="left:50px;top:1523px"><h3>Clinically Trusted</h3><p>Lorem ipsum dolor sit amet consectetur</p></div>
    <div class="feature" style="left:791px;top:1527px"><h3>Premium Comfort</h3><p>Lorem ipsum dolor sit amet consectetur</p></div>
    <div class="feature left" style="left:8px;top:1658px"><h3>Easy to Use &amp; Hygienic</h3><p>Lorem ipsum dolor sit amet consectetur</p></div>
    <div class="feature" style="left:835px;top:1661px"><h3>Premium Comfort</h3><p>Lorem ipsum dolor sit amet consectetur</p></div>
    <div class="feature left" style="left:55px;top:1808px"><h3>Improves Patient Experience</h3><p>Lorem ipsum dolor sit amet consectetur</p></div>
    <div class="feature" style="left:799px;top:1792px"><h3>Premium Comfort</h3><p>Lorem ipsum dolor sit amet consectetur</p></div>
  </section>

  <!-- Technology & Design -->
  <section class="design">
    <div class="photo" role="img" aria-label="Smiling woman having a hearing aid fitted by a clinician" style="left:480px;top:2010px;width:720px;height:601px;background:linear-gradient(100deg,#fff 0%,#e8e6e3 25%,#c9a58a 55%,#d7b58e 75%,#dfe8f1 100%)"></div>
    <div class="eyebrow" style="left:111px;top:2147px">Why choose us</div>
    <h2 class="heading" style="left:109px;top:2172px;font-size:42px;line-height:48px">Technology &amp;<br>Design Excellence</h2>
    <p class="copy" style="left:118px;top:2284px;width:420px">Lorem ipsum dolor sit amet, consectetur adipiscing elit, sed do eiusmod tempor incididunt ut labore et dolore magna aliqua Quis ipsum suspe</p>
    <p class="copy" style="left:118px;top:2384px;width:420px">Lorem ipsum dolor sit amet, consectetur adipiscing elit, sed do eiusmod tempor incididunt.</p>
    <div class="btn" style="left:117px;top:2460px;width:164px;height:42px">Learn more</div>
  </section>

  <!-- Testimonials -->
  <section class="testimonials">
    <div class="abs" style="left:3px;top:2611px;width:1197px;height:622px;background:var(--grey-bg)"></div>
    <div class="eyebrow" style="left:0;width:1218px;text-align:center;top:2666px">Testimonials</div>
    <h2 class="heading" style="left:0;width:1218px;text-align:center;top:2690px;font-size:40px">What People are Saying</h2>
    <div class="t-side" style="left:138px;top:2845px;width:200px;height:188px">"Lorem ipsum dolor sit amet, eiusmod tempor incididunt ipsum suspendisse maecenas</div>
    <div class="t-side" style="left:890px;top:2845px;width:196px;height:188px">adipiscing elit, sed do magna aliqua. Quis commodo viverra facilisis"</div>
    <div class="t-main">
      <p style="position:absolute;left:50px;top:72px;width:543px;font-size:17px;line-height:25px">"Lorem ipsum dolor sit amet, consectetur adipiscing elit, sed do eiusmod tempor incididunt ut labore et dolore magna aliqua. Quis ipsum suspendisse ultrices gravida. Risus commodo viverra maecenas accumsan lacus vel facilisis"</p>
      <p style="position:absolute;left:0;width:643px;top:190px;font-size:17px;font-weight:500">Marion Hatley</p>
      <p style="position:absolute;left:0;width:643px;top:214px;font-size:16px;letter-spacing:3px">&#9733;&#9733;&#9733;&#9733;&#9733;</p>
      <svg style="position:absolute;left:530px;top:185px" width="66" height="52" viewBox="0 0 66 52"><circle cx="15" cy="15" r="14" fill="#fff"/><path d="M27 17 C27 35 18 46 4 50" stroke="#fff" stroke-width="7" fill="none"/><circle cx="48" cy="15" r="14" fill="#fff"/><path d="M60 17 C60 35 51 46 37 50" stroke="#fff" stroke-width="7" fill="none"/></svg>
    </div>
    <div class="photo" role="img" aria-label="Portrait of the reviewer" style="left:566px;top:2755px;width:96px;height:96px;border-radius:50%;border:3px solid #fff;background:linear-gradient(160deg,#e6d2b8,#c6a17c)"></div>
    <div class="arrow" style="left:569px;top:3098px"><svg width="14" height="14" viewBox="0 0 14 14"><path d="M9 2 L4 7 L9 12" stroke="#fff" stroke-width="2" fill="none"/></svg></div>
    <div class="arrow" style="left:625px;top:3098px"><svg width="14" height="14" viewBox="0 0 14 14"><path d="M5 2 L10 7 L5 12" stroke="#fff" stroke-width="2" fill="none"/></svg></div>
  </section>

  <!-- Contact -->
  <section class="contact">
    <div class="eyebrow" style="left:158px;top:3337px">Get in touch</div>
    <h2 class="heading" style="left:155px;top:3363px;font-size:36px">Contact Vorquelin</h2>
    <div class="contact-item" style="top:3440px"><span class="ci-icon"><svg width="16" height="18" viewBox="0 0 16 18"><path d="M8 17 C3 11 2 9 2 6.5 A6 6 0 0 1 14 6.5 C14 9 13 11 8 17Z" fill="#fff"/><circle cx="8" cy="6.5" r="2" fill="var(--beige)"/></svg></span><span>48 Calder Row<br>Suite 12, Ashby, UK AB1 2CD</span></div>
    <div class="contact-item" style="top:3506px"><span class="ci-icon"><svg width="16" height="16" viewBox="0 0 16 16"><path d="M3 1 L6 1 L7 5 L5 6.5 C6 9 7 10 9.5 11 L11 9 L15 10 L15 13 C15 14 14 15 13 15 C6 15 1 10 1 3 C1 2 2 1 3 1Z" fill="#fff"/></svg></span><span>+44 (0)20 0000 0000</span></div>
    <div class="contact-item" style="top:3560px"><span class="ci-icon"><svg width="16" height="12" viewBox="0 0 16 12"><rect x="0.5" y="0.5" width="15" height="11" rx="1" fill="#fff"/><path d="M1 1 L8 7 L15 1" stroke="var(--beige)" stroke-width="1.3" fill="none"/></svg></span><span>info@vorquelin.com</span></div>
    <div class="abs" style="left:525px;top:3328px;width:1px;height:325px;background:#ccc"></div>
    <div class="abs" style="left:522px;top:3469px;width:7px;height:7px;border-radius:50%;background:var(--beige)"></div>

    <div class="abs" style="left:583px;top:3313px;width:490px;height:332px;background:var(--panel)"></div>
    <div class="field" style="left:627px;top:3361px;width:196px;height:38px">First Name</div>
    <div class="field" style="left:832px;top:3361px;width:196px;height:38px">Last Name</div>
    <div class="field" style="left:627px;top:3410px;width:196px;height:38px">Email address</div>
    <div class="field" style="left:832px;top:3410px;width:196px;height:38px">Phone Number</div>
    <div class="field" style="left:627px;top:3461px;width:401px;height:80px">Message</div>
    <div class="btn" style="left:637px;top:3560px;width:162px;height:42px;font-size:12px">Send message</div>
  </section>

  <!-- Footer -->
  <footer class="footer">
    <div class="brand" style="position:absolute;left:115px;top:66px;font-size:36px"><span class="brand-dot" style="width:36px;height:36px"></span>vorquelin</div>
    <p class="abs" style="left:122px;top:132px;width:240px;font-size:11.5px;line-height:17px;color:#444">Lorem ipsum dolor sit amet, consectetur adipiscing elit, sed do eiusmod tempor</p>
    <div class="social" style="position:absolute;left:122px;top:190px"><span style="width:28px;height:28px;background:#666"></span><span style="width:28px;height:28px;background:#999"></span><span style="width:28px;height:28px;background:#999"></span><span style="width:28px;height:28px;background:#999"></span></div>

    <div class="f-title" style="left:402px;top:62px">Navigation</div>
    <ul class="f-list" style="left:405px;top:100px"><li>Home</li><li>For Individuals</li><li>For Clinics</li><li>About</li><li>Support</li><li>Contact</li></ul>

    <div class="f-title" style="left:580px;top:62px">Contact us</div>
    <div class="f-item" style="left:580px;top:100px"><span class="ci-icon"></span><span>48 Calder Row<br>Suite 12, Ashby, UK AB1 2CD</span></div>
    <div class="f-item" style="left:580px;top:146px"><span class="ci-icon"></span><span>+44 (0)20 0000 0000</span></div>
    <div class="f-item" style="left:580px;top:186px"><span class="ci-icon"></span><span>info@vorquelin.com</span></div>

    <div class="f-title" style="left:847px;top:62px">Subscribe Newletter</div>
    <div class="abs" style="left:851px;top:99px;width:213px;height:34px;border:1px solid #ccc;border-radius:17px;background:#fff;font-size:11px;color:#555;padding:10px 18px">Email address</div>
    <div class="abs" style="left:851px;top:146px;width:213px;height:34px;border-radius:17px;background:var(--beige);color:#fff;font-size:12px;display:flex;align-items:center;justify-content:center">Subscribe &#8599;</div>

    <div class="abs" style="left:115px;top:332px;width:955px;height:1px;background:#cfc8b0"></div>
    <p class="abs" style="left:137px;top:356px;font-size:13px;color:#444">Copyright &copy; 2025 vorquelin. All Right Reserved</p>
    <p class="abs" style="left:799px;top:354px;font-size:13px;color:#444;word-spacing:2px">Terms of Use &nbsp; Privacy Policy &nbsp; Disclaimer</p>
  </footer>

</div>
</body>
</html>
```